Design a Website Mockup for Vivid Hue Lab

Hi All,

- I have this website for acrylic sheet print, now the client did a logo that I don't like. So I want to have the same concept, still more modern.

- I want to brand the site according to the logo. So after you make the logo, I want you to brand the site according to the logo.

So I need a web design:

1) home page
2) inner page content
3) product page
4) contact us page

development link: [login to view URL]

Note: For the mockup web design, you have to stay with the elements of this theme.

- go crazy with the research if it needed.

Only entries that respect this rule will be considered.

The client has three products:

1) Acrylic Sheet Print
2) Metal Print Mount Option
3) Foam board Poster Print

picture link:

Note: If you need more pictures, let me know.

I need a web a design, I will do the development

Good Luck to all

```html
<!DOCTYPE html>
<html lang="en">
<head>
<meta charset="utf-8">
<title>Vivid Hue Lab — Acrylic Sheet Print</title>
<link href="https://fonts.googleapis.com/css2?family=Open+Sans:wght@400;600;700&family=Pacifico&display=swap" rel="stylesheet">
<style>
:root{
  --blue:#2f3a9a;
  --orange:#f7941d;
  --ink:#222;
  --muted:#777;
  --line:#cfcfcf;
  --grey:#e4e1e1;
  --dark:#1f1f1f;
  --darker:#141414;
  --white:#fff;
}
*{box-sizing:border-box;margin:0;padding:0}
html,body{width:1200px;height:5056px;overflow:hidden;background:#fff}
body{font-family:"Open Sans",Arial,sans-serif;color:var(--ink)}
.canvas{position:relative;width:1200px;height:5056px;overflow:hidden}
.abs{position:absolute}
.ph{position:absolute}
.dot{display:inline-block;border-radius:50%}

/* top bar */
.topbar{top:0;left:0;width:1200px;height:40px;border-bottom:1px solid #eee}
.topbar .social{left:106px;top:13px;display:flex;gap:22px}
.topbar .social span{width:12px;height:12px;background:#333;border-radius:50%}
.topbar .links{right:106px;top:0;height:40px;display:flex;font-size:10px;color:#666}
.topbar .links div{padding:0 20px;line-height:40px;border-left:1px solid #eee}

/* header */
.header{top:40px;left:0;width:1200px;height:105px}
.brand{left:106px;top:38px;display:flex;align-items:center;gap:10px;font-weight:700;font-size:22px;color:var(--blue)}
.brand i{width:26px;height:26px;background:var(--orange);display:block}
.nav{left:405px;top:44px;display:flex;gap:30px;font-size:12px;font-weight:600;color:#333}
.order{left:928px;top:36px;width:122px;height:38px;border-radius:19px;background:var(--blue);color:#fff;font-size:13px;font-weight:600;text-align:center;line-height:38px}
.search{left:1074px;top:44px}

/* hero */
.hero{top:145px;left:0;width:1200px;height:542px;background:linear-gradient(180deg,#f6efe6 0%,#efe2d0 70%,#c9a47e 100%)}
.hero .kicker{left:150px;top:120px;font-size:17px;font-weight:600;color:#222;line-height:24px}
.hero h1{left:106px;top:146px;font-family:"Pacifico",cursive;font-weight:400;font-size:42px;line-height:56px;color:var(--blue);white-space:nowrap}
.hero .sub{left:172px;top:212px;font-size:13px;line-height:18px;color:var(--orange)}
.hero .cta{left:216px;top:260px;width:162px;height:46px;border-radius:23px;background:var(--orange);color:#fff;font-size:13px;text-align:center;line-height:46px}

/* section headings */
.sec-title{left:0;width:1200px;text-align:center;font-size:25px;font-weight:600}
.sec-title::before,.sec-title::after{content:"";position:absolute;top:50%;width:305px;height:1px;background:var(--line)}
.sec-title::before{left:110px}.sec-title::after{right:110px}
.sec-sub{left:0;width:1200px;text-align:center;font-size:12px;color:#999}

/* tabs */
.tabs{left:310px;top:830px;display:flex}
.tabs div{width:194px;height:48px;border:1px solid #ccc;font-size:12px;line-height:46px;text-align:center;color:#666;font-weight:600}
.tabs .on{background:var(--orange);color:#fff;border-color:var(--orange)}

.pcard{left:106px;top:913px;width:402px;height:540px;border:2px solid #ddd;background:#fff}
.pcard .img{left:22px;top:22px;width:356px;height:404px;background:linear-gradient(180deg,#5b5f9e,#9a8aa5 50%,#e89a3c)}
.pcard .zoom{left:164px;top:189px;width:70px;height:70px;border-radius:50%;background:var(--orange)}
.pcard h3{left:0;top:436px;width:100%;text-align:center;font-size:16px;font-weight:600;letter-spacing:.5px}
.pcard .small{left:0;top:461px;width:100%;text-align:center;font-size:10px;color:#999}
.pcard .cart{left:20px;top:491px;width:124px;height:30px;border:1px solid #ccc;font-size:12px;line-height:28px;padding-left:40px}
.pcard .cart i{position:absolute;left:0;top:0;width:32px;height:28px;background:var(--orange)}
.pcard .old{left:254px;top:491px;width:62px;height:30px;border:1px solid #ccc;text-align:center;line-height:28px;font-size:13px;color:#c33;text-decoration:line-through}
.pcard .price{left:316px;top:491px;width:64px;height:30px;background:var(--orange);color:#fff;text-align:center;line-height:30px;font-size:17px;font-weight:600}

.tile{border:1px solid #ccc}
.more{position:absolute;left:50%;bottom:20px;transform:translateX(-50%);width:116px;height:30px;border-radius:15px;background:var(--blue);color:#fff;border:2px solid #fff;font-size:12px;text-align:center;line-height:26px}

/* service */
.service{top:1555px;left:0;width:1200px;height:364px;background:var(--blue);color:#fff}
.service h2{left:106px;top:52px;width:534px;text-align:center;font-size:24px;font-weight:600}
.service h2::before,.service h2::after{content:"";position:absolute;top:50%;width:165px;height:1px;background:#aab}
.service h2::before{left:0}.service h2::after{right:0}
.service .lead{left:106px;top:92px;width:534px;text-align:center;font-size:12px}
.svc{width:240px;font-size:11px;line-height:16px}
.svc b{display:block;color:var(--orange);font-size:12px;font-weight:600;margin-bottom:6px}
.service .frame{left:687px;top:-26px;width:404px;height:414px;background:#fff;border-top:6px solid #111;border-bottom:6px solid #111;padding:6px}

/* projects */
.filters{left:226px;top:2045px;display:flex;gap:16px}
.filters div{height:36px;border-radius:18px;border:2px solid #ccc;font-size:12px;line-height:32px;padding:0 22px;color:#555;display:flex;align-items:center;gap:8px}
.filters div i{width:10px;height:10px;border-radius:50%;background:#888}
.filters .on{background:var(--orange);border-color:var(--orange);color:#222}
.filters .on i{background:#222}
.btn-out{width:200px;height:48px;border:2px solid #3a3f7a;border-radius:24px;text-align:center;line-height:44px;font-size:12px;color:#333}

/* promo */
.promo{top:2558px;left:0;width:1200px;height:543px;background:var(--grey)}
.offer{left:418px;top:151px;width:363px;height:239px;background:#fff;padding:16px}
.offer .inner{width:100%;height:100%;border:1px solid #aaa;text-align:center}
.offer .pct{font-size:34px;font-weight:700;margin-top:20px}
.offer .pct span{color:var(--orange);font-weight:600}
.offer .rule{width:290px;height:3px;border-top:1px solid #555;border-bottom:1px solid #555;margin:8px auto 12px}
.offer .ship{font-size:26px;letter-spacing:7px;margin-top:8px}

/* clients */
.logos{left:106px;top:3215px;width:985px;display:flex;justify-content:space-between;align-items:center}
.logos div{display:flex;align-items:center;gap:10px;font-size:24px;font-weight:600;color:#555}
.logos i{width:22px;height:22px;background:#3d6fb5;display:block}
.testi{width:298px;height:86px;background:#fff;box-shadow:0 2px 8px rgba(0,0,0,.18);font-size:11px;line-height:17px;color:#666;padding:14px 20px}
.testi::after{content:"";position:absolute;left:54px;bottom:-18px;border:18px solid transparent;border-top-color:#fff;border-bottom:0}
.person{display:flex;align-items:center;gap:26px}
.person .av{width:70px;height:70px;border-radius:50%;background:linear-gradient(#d9c7b8,#9a7f6d)}
.person b{display:block;font-size:12px;font-weight:600;color:#333}
.person em{font-size:10px;color:#999}

/* news */
.news{top:3647px;left:0;width:1200px;height:609px;background:var(--blue)}
.news h2{left:0;top:52px;width:1200px;text-align:center;font-size:25px;font-weight:600;color:#fff}
.ncard{top:114px;width:312px;height:365px;background:#fff}
.ncard .ph{left:0;top:0;width:312px;height:214px}
.ncard .meta{left:0;top:214px;width:312px;height:39px;border-bottom:1px solid #ddd;display:flex;justify-content:space-between;align-items:center;padding:0 10px;font-size:12px;color:#555}
.ncard .meta span{display:flex;align-items:center;gap:6px}
.ncard h4{left:0;top:270px;width:312px;text-align:center;color:var(--orange);font-size:12px;font-weight:600}
.ncard p{left:14px;top:290px;width:284px;font-size:11px;line-height:17px;color:#555}
.arrow{width:48px;height:48px;border-radius:50%;border:2px solid #fff;background:rgba(255,255,255,.1)}
.news .btn-out{border-color:#fff;color:#fff}

/* newsletter */
.nl-title{left:0;top:4320px;width:1200px;text-align:center;font-size:24px;font-weight:700}
.nl-sub{left:0;top:4360px;width:1200px;text-align:center;font-size:12px;color:#666}
.nl-input{left:267px;top:4399px;width:530px;height:52px;border:1px solid #2f3a9a;border-right:0}
.nl-btn{left:797px;top:4399px;width:137px;height:52px;background:var(--blue);color:#fff;text-align:center;line-height:52px;font-size:12px;font-weight:600}
.nl-social{left:506px;top:4480px;display:flex;align-items:center;gap:10px;font-size:11px;font-weight:700}
.nl-social i{width:16px;height:16px;border-radius:50%;background:var(--blue);display:block}

/* footer */
.footer{top:4554px;left:0;width:1200px;height:438px;background:var(--dark);color:#ddd}
.footer h5{font-size:15px;font-weight:400;color:#fff;letter-spacing:.4px}
.footer .about{left:106px;top:156px;width:318px;font-size:11px;line-height:18px;color:#d98a2b}
.footer .follow{left:106px;top:236px;width:318px;border-top:1px solid #555;padding-top:16px}
.footer .follow div{display:flex;gap:12px;margin-top:10px}
.footer .follow i{width:24px;height:24px;border-radius:50%;border:2px solid #fff;display:block}
.fp{font-size:10px;line-height:16px;color:#ddd}
.fp .th{position:absolute;right:0;top:0;width:52px;height:32px;background:linear-gradient(135deg,#999,#e6e6e6)}
.posts li{list-style:none;font-size:10px;line-height:27px;color:#ddd}
.posts li::before{content:"›";color:var(--orange);margin-right:6px}
.contact div{font-size:10px;line-height:16px;margin-bottom:10px;padding-left:22px;position:relative;word-break:break-all}
.contact div i{position:absolute;left:0;top:2px;width:10px;height:10px;border-radius:50%;background:#ddd}
.insta{left:476px;top:331px;display:flex;gap:8px}
.insta div{width:94px;height:84px}
.copy{top:4992px;left:0;width:1200px;height:64px;background:var(--darker);color:#ddd;text-align:center;line-height:64px;font-size:12px}
</style>
</head>
<body>
<div class="canvas">

  <div class="abs topbar">
    <div class="abs social"><span></span><span></span><span></span><span></span><span></span></div>
    <div class="abs links"><div>Shopping Cart</div><div>My Account ⌄</div><div>🛒 Cart ⌄</div></div>
  </div>

  <header class="abs header">
    <div class="abs brand"><i></i>Vivid Hue Lab</div>
    <nav class="abs nav"><span>Home ⌄</span><span>Our Products ⌄</span><span>News Services ⌄</span><span>About Us</span><span>Contact Us</span></nav>
    <div class="abs order">Order Now</div>
    <svg class="abs search" width="16" height="16" viewBox="0 0 16 16"><circle cx="6.5" cy="6.5" r="5" fill="none" stroke="#222" stroke-width="2"/><line x1="10" y1="10" x2="15" y2="15" stroke="#222" stroke-width="2"/></svg>
  </header>

  <section class="abs hero">
    <div class="ph" role="img" aria-label="Multi-panel surreal art print on the wall" style="left:510px;top:47px;width:390px;height:182px;background:linear-gradient(90deg,#bdbdbd,#7a7a7a,#d6d6d6)"></div>
    <div class="ph" role="img" aria-label="Bare branch in a white vase" style="left:1030px;top:20px;width:170px;height:420px;background:linear-gradient(180deg,rgba(120,90,70,.15),rgba(255,255,255,.7))"></div>
    <div class="ph" role="img" aria-label="Brown leather sofa with a white coffee table" style="left:340px;top:322px;width:640px;height:220px;background:linear-gradient(180deg,#7a4b2b,#4d2d19)"></div>
    <div class="abs kicker">Lorem Ipsum is simply dummy text</div>
    <h1 class="abs">Acrylic sheet print</h1>
    <div class="abs sub">Make your print glass the way you want</div>
    <div class="abs cta">Choose a Product</div>
  </section>

  <h2 class="abs sec-title" style="top:748px">Featured Products</h2>
  <div class="abs sec-sub" style="top:790px">Must have products from our top sellers</div>
  <div class="abs tabs"><div class="on">ACRYLIC SHEET PRINT</div><div>ACRYLIC SHEET PRINT</div><div>ACRYLIC SHEET PRINT</div></div>

  <div class="abs pcard">
    <div class="ph img" role="img" aria-label="Product print under acrylic glass"></div>
    <svg class="abs zoom" viewBox="0 0 70 70"><circle cx="31" cy="31" r="12" fill="none" stroke="#fff" stroke-width="4"/><line x1="40" y1="40" x2="50" y2="50" stroke="#fff" stroke-width="5"/></svg>
    <h3 class="abs">PRINT UNDER ACRYLIC GLASS</h3>
    <div class="abs small">Must have products from our top sellers</div>
    <div class="abs cart"><i></i>Add to Cart</div>
    <div class="abs old">$235</div>
    <div class="abs price">$200</div>
  </div>

  <div class="ph tile" role="img" aria-label="Glass sphere on cracked earth" style="left:610px;top:913px;width:231px;height:260px;background:linear-gradient(160deg,#8b6a4a,#2c8fa0,#5a4632)"><div class="more">More Info</div></div>
  <div class="ph tile" role="img" aria-label="Surreal rock landscape at dusk" style="left:860px;top:913px;width:231px;height:260px;background:linear-gradient(180deg,#1f2f6e,#a65f3a,#3a3a5a)"><div class="more">More Info</div></div>
  <div class="ph tile" role="img" aria-label="Abstract red and silver shapes" style="left:610px;top:1190px;width:231px;height:260px;background:linear-gradient(160deg,#4a7a78,#b23030,#d8d0c0)"><div class="more">More Info</div></div>
  <div class="ph tile" role="img" aria-label="Surreal stage scene with red curtains" style="left:860px;top:1190px;width:231px;height:260px;background:linear-gradient(180deg,#f28a2a,#8a1f1f,#3a4560)"><div class="more">More Info</div></div>

  <section class="abs service">
    <h2 class="abs">Our Service</h2>
    <div class="abs lead">Lorem ipsum dolor sit amet, consectetur adipisicing elit, sed do eiusmod.</div>
    <div class="abs svc" style="left:106px;top:146px"><b>PRINT UNDER ACRYLIC GLASS</b>Lorem ipsum dolor sit amet, consectetuer adipiscing elit, sed diam nonummyading elit, sed diam.</div>
    <div class="abs svc" style="left:440px;top:146px"><b>METAL PRINT UNDER ACRYLIC</b>Lorem ipsum dolor sit amet, consectetuer adipiscing elit, sed diam nonummyading elit, sed diam.</div>
    <div class="abs svc" style="left:106px;top:258px"><b>FOAM BOARD POSTER PRINT</b>Lorem ipsum dolor sit amet, consectetuer adipiscing elit, sed diam nonummyading elit, sed diam.</div>
    <div class="abs svc" style="left:440px;top:258px"><b>DEMO POSTER PRINT</b>Lorem ipsum dolor sit amet, consectetuer adipiscing elit, sed diam nonummyading elit, sed diam.</div>
    <div class="abs frame"><div role="img" aria-label="Chrome abstract sculpture with red spheres" style="width:100%;height:100%;background:linear-gradient(160deg,#f2f2f2,#9a9a9a,#e0e0e0)"></div></div>
  </section>

  <h2 class="abs sec-title" style="top:1984px">Our Projects</h2>
  <div class="abs filters"><div class="on"><i></i>Print under acrylic glass</div><div><i></i>Metal Print Under Acrylic</div><div><i></i>Foam board Poster Print</div></div>

  <div class="ph" role="img" aria-label="Surreal sunset scene" style="left:106px;top:2106px;width:239px;height:155px;background:linear-gradient(180deg,#e08a50,#6a6a90)"><span class="abs" style="left:16px;top:106px;color:#fff;font-size:17px">Under acrylic glass</span><span class="abs dot" style="left:188px;top:100px;width:32px;height:32px;background:var(--orange)"></span></div>
  <div class="ph" role="img" aria-label="Melting clock landscape" style="left:353px;top:2106px;width:242px;height:155px;background:linear-gradient(180deg,#4f86c6,#c9a26a)"></div>
  <div class="ph" role="img" aria-label="Lake at dusk" style="left:603px;top:2106px;width:241px;height:155px;background:linear-gradient(180deg,#2a3a7a,#c46a3a)"></div>
  <div class="ph" role="img" aria-label="Surreal portrait in the desert" style="left:852px;top:2106px;width:239px;height:155px;background:linear-gradient(180deg,#c7b89a,#a06030)"></div>
  <div class="ph" role="img" aria-label="Red ring sculpture" style="left:106px;top:2271px;width:239px;height:153px;background:linear-gradient(160deg,#eee,#b01818,#ddd)"></div>
  <div class="ph" role="img" aria-label="Lion on a checkered floor" style="left:353px;top:2271px;width:242px;height:153px;background:linear-gradient(160deg,#ddd,#8a6a40,#444)"></div>
  <div class="ph" role="img" aria-label="Floating cubes" style="left:603px;top:2271px;width:241px;height:153px;background:linear-gradient(160deg,#f0f0f0,#bbb,#c03030)"></div>
  <div class="ph" role="img" aria-label="Abstract teal and red forms" style="left:852px;top:2271px;width:239px;height:153px;background:linear-gradient(160deg,#2a8a90,#d8c8a8,#a02020)"></div>

  <div class="abs btn-out" style="left:502px;top:2450px">View all project</div>

  <section class="abs promo">
    <div class="ph" role="img" aria-label="Surreal elephants in a red desert" style="left:106px;top:61px;width:436px;height:414px;background:linear-gradient(180deg,#d87a30,#5a3a30 55%,#b8381a)"></div>
    <div class="ph" role="img" aria-label="Dice and spheres in a silver room" style="left:571px;top:108px;width:520px;height:320px;background:linear-gradient(160deg,#333,#aaa,#e8e8e8)"></div>
    <div class="abs offer"><div class="inner">
      <div class="pct">70% <span>OFF</span></div>
      <div class="rule"></div>
      <svg width="60" height="36" viewBox="0 0 60 36"><rect x="14" y="6" width="28" height="18" fill="#222"/><path d="M42 11h9l6 7v6H42z" fill="#222"/><circle cx="22" cy="28" r="4" fill="#222"/><circle cx="49" cy="28" r="4" fill="#222"/><line x1="2" y1="10" x2="12" y2="10" stroke="#222" stroke-width="2"/><line x1="0" y1="16" x2="12" y2="16" stroke="#222" stroke-width="2"/></svg>
      <div class="ship">FREE SHIPPING</div>
    </div></div>
  </section>

  <h2 class="abs sec-title" style="top:3156px">Clients &amp; Testimonials</h2>
  <div class="abs logos">
    <div><i></i>Northgate Press</div><div><i></i>Clarivent</div><div><i></i>Orbita Finance</div><div><i></i>Linewell</div><div><i></i>Ridgeway</div>
  </div>

  <div class="abs testi" style="left:106px;top:3361px">Lorem ipsum dolor sit amet, consectetur adipisicing elit, sed do eiusmod tempor incididunt ut labore et dolore magna aliqua.</div>
  <div class="abs testi" style="left:450px;top:3361px">Lorem ipsum dolor sit amet, consectetur adipisicing elit, sed do eiusmod tempor incididunt ut labore et dolore magna aliqua.</div>
  <div class="abs testi" style="left:793px;top:3361px">Lorem ipsum dolor sit amet, consectetur adipisicing elit, sed do eiusmod tempor incididunt ut labore et dolore magna aliqua.</div>

  <div class="abs person" style="left:140px;top:3484px"><div class="av" role="img" aria-label="Client portrait"></div><div><b>DANA WELLS</b><em>Multinational Company</em></div></div>
  <div class="abs person" style="left:492px;top:3484px"><div class="av" role="img" aria-label="Client portrait"></div><div><b>OWEN HALE</b><em>Developer</em></div></div>
  <div class="abs person" style="left:836px;top:3484px"><div class="av" role="img" aria-label="Client portrait"></div><div><b>LENA MARSH</b><em>Web Designer</em></div></div>

  <div class="abs" style="left:582px;top:3578px;display:flex;gap:5px"><span class="dot" style="width:9px;height:9px;background:#888"></span><span class="dot" style="width:9px;height:9px;border:1px solid #888"></span><span class="dot" style="width:9px;height:9px;border:1px solid #888"></span></div>

  <section class="abs news">
    <h2 class="abs">News</h2>
    <div class="abs arrow" style="left:48px;top:284px"><svg width="44" height="44" viewBox="0 0 44 44"><path d="M25 15l-7 7 7 7" fill="none" stroke="#fff" stroke-width="2"/></svg></div>
    <div class="abs arrow" style="left:1100px;top:284px"><svg width="44" height="44" viewBox="0 0 44 44"><path d="M19 15l7 7-7 7" fill="none" stroke="#fff" stroke-width="2"/></svg></div>

    <article class="abs ncard" style="left:106px">
      <div class="ph" role="img" aria-label="Dice sculpture in a silver room" style="background:linear-gradient(160deg,#444,#ccc,#b02020)"></div>
      <div class="abs meta"><span><i class="dot" style="width:12px;height:12px;background:var(--orange)"></i>Admin</span><span><i style="width:12px;height:12px;border:2px solid var(--orange);display:block"></i>15 June,2018</span></div>
      <h4 class="abs">AENEAN LOBORTIS SAPIEN ENIM VIVERRA</h4>
      <p class="abs">Lorem ipsum dolor sit amet, consectetur adipiscing elit, sed do eiusmod tempor incididunt ut labore et dolore magna aliqua.</p>
    </article>
    <article class="abs ncard" style="left:444px">
      <div class="ph" role="img" aria-label="Surreal beach scene with drapery" style="background:linear-gradient(180deg,#5aa8d8,#c84030,#e0d0b0)"></div>
      <div class="abs meta"><span><i class="dot" style="width:12px;height:12px;background:var(--orange)"></i>Admin</span><span><i style="width:12px;height:12px;border:2px solid var(--orange);display:block"></i>15 June,2018</span></div>
      <h4 class="abs">DUIS AC MASSA SEMPER MAXIMUS</h4>
      <p class="abs">Lorem ipsum dolor sit amet, consectetur adipiscing elit, sed do eiusmod tempor incididunt ut labore et dolore magna aliqua.</p>
    </article>
    <article class="abs ncard" style="left:781px">
      <div class="ph" role="img" aria-label="Red ring sculpture" style="background:linear-gradient(160deg,#eee,#b01818,#ddd)"></div>
      <div class="abs meta"><span><i class="dot" style="width:12px;height:12px;background:var(--orange)"></i>Admin</span><span><i style="width:12px;height:12px;border:2px solid var(--orange);display:block"></i>15 June,2018</span></div>
      <h4 class="abs">NUNC FERMINT NULLA EU JUSTO SEM ID</h4>
      <p class="abs">Lorem ipsum dolor sit amet, consectetur adipiscing elit, sed do eiusmod tempor incididunt ut labore et dolore magna aliqua.</p>
    </article>

    <div class="abs btn-out" style="left:502px;top:511px">More news</div>
  </section>

  <h2 class="abs nl-title">SUBSCRIBE OUR NEWSLETTER!</h2>
  <div class="abs nl-sub">To Get Update &amp; Discount From Shop</div>
  <div class="abs nl-input"></div>
  <div class="abs nl-btn">SIGN UP</div>
  <div class="abs nl-social">OR SIGN UP ON <i></i><i></i><i></i></div>

  <footer class="abs footer">
    <div class="abs brand" style="top:52px;color:#fff"><i></i>Vivid Hue Lab</div>
    <p class="abs about">Lorem ipsum dolor sit amet, consectetur adipiscing elit, sed do eiusmod tempor incididunt ut labore et dolore magna aliqua. Ut enim ad minim veniam, quis nostrud exercitation ullamco laboris nisi ut aliquip ex ea commodo consequat.</p>
    <div class="abs follow"><h5>Follow us on:</h5><div><i></i><i></i><i></i><i></i><i></i></div></div>

    <h5 class="abs" style="left:476px;top:56px">TOP RATED PRODUCTS</h5>
    <div class="abs fp" style="left:476px;top:92px;width:208px">Print under acrylic glass<br>$25.00 – $89.00<i class="th"></i></div>
    <div class="abs fp" style="left:476px;top:144px;width:208px">Metal Print Under Acrylic<br>$45.00 – $109.00<i class="th"></i></div>
    <div class="abs fp" style="left:476px;top:196px;width:208px">Foam board Poster Print<br>$9.00 – $36.00<i class="th"></i></div>

    <h5 class="abs" style="left:729px;top:56px">RECENT POSTS</h5>
    <ul class="abs posts" style="left:731px;top:84px">
      <li>Aenean lobortis sapien enim viverra</li><li>Duis ac massa semper maximus</li><li>Nunc fermint nulla eu justo sem id</li><li>Aliquam posuere magna eget nibh</li><li>Cras ac nulla ac consecte rutrum</li><li>Fusce mattis nunc ut aliquam</li>
    </ul>

    <h5 class="abs" style="left:941px;top:56px">CONTACTS</h5>
    <div class="abs contact" style="left:941px;top:92px;width:160px">
      <div><i></i>240 Elm Row,<br>Riverton, QC H0H 0A0</div>
      <div><i></i>Email: hello@vividhuelab.example</div>
      <div><i></i>+1 555 010 2847</div>
    </div>

    <h5 class="abs" style="left:476px;top:300px">Instagram</h5>
    <div class="abs insta">
      <div role="img" aria-label="Gallery print thumbnail" style="background:linear-gradient(160deg,#eee,#b01818)"></div>
      <div role="img" aria-label="Gallery print thumbnail" style="background:linear-gradient(160deg,#ddd,#888)"></div>
      <div role="img" aria-label="Gallery print thumbnail" style="background:linear-gradient(160deg,#555,#ccc)"></div>
      <div role="img" aria-label="Gallery print thumbnail" style="background:linear-gradient(160deg,#eee,#c03030)"></div>
      <div role="img" aria-label="Gallery print thumbnail" style="background:linear-gradient(180deg,#4f86c6,#c9a26a)"></div>
      <div role="img" aria-label="Gallery print thumbnail" style="background:linear-gradient(160deg,#f0e0d0,#b02020)"></div>
    </div>
  </footer>
  <div class="abs copy">© Copyright - 2018 &nbsp;|&nbsp; All Rights Reserved</div>

</div>
</body>
</html>
```